Business Card Design

Plumbing business.
Looking for a simple but professional looking design.
There are two variations of the logo; white background and black background. The logo with the white background is the primary business logo.
Industry/Entity Type
Business
Contact Information for Business Card
Marcus Fenley
Owner/Licensed Plumber
0412 396 081
info@marcusfenleyplumbing.com.au
www.marcusfenleyplumbing.com.au
Lic. 63941
Look and feel
Each slider illustrates characteristics of the customer's brand and the style your logo design should communicate.

```html
<!DOCTYPE html>
<html lang="en">
<head>
<meta charset="utf-8">
<title>Marcus Fenley Plumbing – Business Card</title>
<link rel="stylesheet" href="https://fonts.googleapis.com/css2?family=Open+Sans:wght@400;600&display=swap">
<style>
  :root {
    --backdrop: #2b2b2b;
    --teal: #27a9b7;
    --teal-deep: #1f95a2;
    --paper: #ffffff;
    --ink: #2a2a2a;
    --ink-soft: #444444;
  }
  * { box-sizing: border-box; margin: 0; padding: 0; }
  html, body {
    width: 1200px; height: 900px; overflow: hidden;
    background: var(--backdrop);
    font-family: "Open Sans", Arial, sans-serif;
  }
  .canvas {
    position: relative; width: 1200px; height: 900px;
    display: flex; flex-direction: column; align-items: center; justify-content: center; gap: 40px;
  }
  .card {
    position: relative; width: 620px; height: 380px;
    box-shadow: 0 10px 30px rgba(0,0,0,0.45);
    overflow: hidden;
  }
  .card--back { background: var(--teal); }
  .card--front { background: var(--paper); }

  .brand { display: flex; align-items: center; gap: 16px; }
  .brand__mark { width: 46px; height: 46px; flex: none; }
  .brand__name {
    font-weight: 600; font-size: 24px; letter-spacing: 0.06em;
    text-transform: uppercase; line-height: 1.15;
  }

  .card--back .brand { position: absolute; left: 268px; top: 150px; }
  .card--back .brand__mark { background: var(--paper); }
  .card--back .brand__name { color: var(--paper); }
  .back__accent {
    position: absolute; left: -60px; top: 150px; width: 280px; height: 280px;
    background: var(--teal-deep); border-radius: 50%;
  }

  .card--front .brand { position: absolute; left: 52px; top: 90px; }
  .card--front .brand__mark { background: var(--teal); }
  .card--front .brand__name { color: var(--ink); }

  .licence {
    position: absolute; right: 34px; top: 26px;
    font-size: 12px; color: var(--ink-soft);
  }
  .person { position: absolute; left: 52px; top: 196px; }
  .person__name {
    color: var(--teal); font-size: 24px; font-weight: 400;
    text-transform: uppercase; letter-spacing: 0.02em;
  }
  .person__role { color: var(--ink); font-size: 15px; margin-top: 2px; }
  .contact {
    position: absolute; left: 52px; top: 278px;
    list-style: none; color: var(--ink); font-size: 16px; line-height: 1.6;
  }
</style>
</head>
<body>
<main class="canvas">
  <section class="card card--back" aria-label="Card back">
    <div class="back__accent"></div>
    <div class="brand">
      <span class="brand__mark"></span>
      <span class="brand__name">Marcus Fenley<br>Plumbing</span>
    </div>
  </section>

  <section class="card card--front" aria-label="Card front">
    <p class="licence">Lic. 63941</p>
    <div class="brand">
      <span class="brand__mark"></span>
      <span class="brand__name">Marcus Fenley<br>Plumbing</span>
    </div>
    <div class="person">
      <h1 class="person__name">Marcus Fenley</h1>
      <p class="person__role">Owner/Licensed Plumber</p>
    </div>
    <ul class="contact">
      <li>0412 396 081</li>
      <li>info@marcusfenleyplumbing.com.au</li>
      <li>www.marcusfenleyplumbing.com.au</li>
    </ul>
  </section>
</main>
</body>
</html>
```